Post Lockdown Ortho Special

We are running a special for (Ortho) Braces/Clear Aligner (Quorventa), till July 31st 2020. Up to $2,000 off with free Consultation and Xrays.

We need a ad to run in different formats.

Maybe something with: what better time to get braces when you have to wear a mask all the time.

Trying to rebuild our business and get people in for free consultations.

```html
<!DOCTYPE html>
<html lang="en">
<head>
<meta charset="utf-8">
<title>Pinecrest Family Dentistry – Post Lockdown Ortho Special</title>
<link href="https://fonts.googleapis.com/css2?family=Rubik:wght@400;500;700;900&display=swap" rel="stylesheet">
<style>
  :root{
    --purple:#6a4399;
    --olive:#a4a152;
    --olive-dark:#8f8c3e;
    --lavender:#d9cfe6;
    --cream:#e6e3cb;
    --white:#ffffff;
    --stage:#efefef;
  }
  *{box-sizing:border-box;margin:0;padding:0}
  html,body{width:1200px;height:800px;overflow:hidden;background:var(--stage)}
  body{font-family:"Rubik",sans-serif;position:relative}
  .flyer{position:absolute;left:330px;top:20px;width:540px;height:760px;background:var(--white);overflow:hidden}
  .flyer-shapes{position:absolute;inset:0}
  .abs{position:absolute}

  .brand{left:32px;top:34px;display:flex;align-items:center;gap:10px}
  .brand-dot{width:44px;height:44px;border-radius:50%;background:var(--purple)}
  .brand-name{font-weight:500;color:var(--purple);font-size:16px;line-height:1.15;letter-spacing:.5px}
  .brand-doctor{left:86px;top:78px;font-size:8px;letter-spacing:1.4px;color:var(--purple);text-transform:uppercase}

  .headline{left:31px;top:132px;font-weight:900;font-size:41px;line-height:41px;text-transform:uppercase;letter-spacing:-.5px}
  .headline .p{color:var(--purple)}
  .headline .w{color:var(--white)}
  .tagline{left:32px;top:302px;color:var(--white);font-size:11px;line-height:14px;font-weight:500;width:200px}

  .offer{left:347px;top:277px;width:160px;height:160px;border-radius:50%;background:var(--purple);border:2px solid var(--olive);color:var(--white);text-align:center;font-weight:900;padding-top:26px}
  .offer-line{font-size:27px;line-height:31px}
  .offer-date{font-size:10px;font-weight:500;margin-top:6px}

  .section-tab{left:0;top:395px;width:212px;height:29px}
  .section-title{left:31px;top:400px;color:var(--white);font-size:15px;font-weight:500}

  .service{width:230px}
  .service-icon{position:absolute;left:0;top:0;width:37px;height:37px;border-radius:50%;display:flex;align-items:center;justify-content:center}
  .service-icon.is-olive{background:var(--olive)}
  .service-icon.is-purple{background:var(--purple)}
  .service-text{margin-left:49px}
  .service-title{color:var(--olive-dark);font-size:14.5px;font-weight:500;line-height:17px}
  .service-body{color:var(--purple);font-size:10.5px;line-height:13px}

  .round-clock{left:31px;top:582px;color:var(--olive-dark);font-size:14px;line-height:17px;width:230px}
  .round-clock-rule{left:31px;top:619px;width:50px;height:1px;background:var(--olive-dark)}
  .about{left:271px;top:577px;width:230px;color:var(--purple);font-size:10.5px;line-height:13px}

  .site-rule{left:0;top:652px;width:540px;height:1px;background:var(--purple);opacity:.6}
  .site-pill{left:172px;top:639px;width:196px;height:26px;border-radius:13px;background:var(--purple);color:var(--white);font-size:12.5px;font-weight:500;text-align:center;line-height:26px}

  .consult-icon{left:33px;top:683px;width:22px;height:22px;border-radius:50%;background:var(--purple)}
  .consult-label{left:64px;top:684px;color:var(--olive-dark);font-size:14px;font-weight:500}
  .consult-phone{left:63px;top:703px;color:var(--purple);font-size:22px;font-weight:700}

  .contact-list{left:271px;top:669px;list-style:none}
  .contact-list li{display:flex;align-items:flex-start;gap:8px;color:var(--purple);font-size:9.5px;line-height:11.5px;margin-bottom:3px}
  .contact-icon{flex:none;width:13px;height:13px;border-radius:50%;border:1.4px solid var(--olive);margin-top:1px;display:flex;align-items:center;justify-content:center}
</style>
</head>
<body>
<main class="flyer">
  <svg class="flyer-shapes" width="540" height="760" viewBox="0 0 540 760" aria-hidden="true">
    <defs>
      <radialGradient id="teamTone" cx="50%" cy="45%" r="60%">
        <stop offset="0%" stop-color="#f3f1ee"/>
        <stop offset="55%" stop-color="#dcdad6"/>
        <stop offset="100%" stop-color="#a9b4c4"/>
      </radialGradient>
      <clipPath id="lowerBand"><rect x="0" y="424" width="540" height="336"/></clipPath>
    </defs>
    <g clip-path="url(#lowerBand)">
      <rect x="0" y="424" width="540" height="336" fill="#d9cfe6"/>
      <polygon points="0,424 540,424 270,600" fill="#e6e3cb"/>
      <polygon points="0,760 540,760 270,600" fill="#e6e3cb"/>
    </g>
    <circle cx="359" cy="197" r="166" fill="url(#teamTone)" role="img" aria-label="Photo of three smiling dental staff, a senior dentist with clipboard in the centre"/>
    <circle cx="104" cy="237" r="141" fill="#a4a152" opacity=".94"/>
  </svg>

  <div class="abs brand">
    <span class="brand-dot"></span>
    <span class="brand-name">Pinecrest<br>Family Dentistry</span>
  </div>
  <p class="abs brand-doctor">Dr Maren Oakley</p>

  <h1 class="abs headline">
    <span class="p">Your</span><br>
    <span class="w">Smile</span><br>
    <span class="p">Is</span> <span class="w">Our</span><br>
    <span class="p">Priority</span>
  </h1>
  <p class="abs tagline">What better time to get braces than<br>while you wear a mask all the time?</p>

  <div class="abs offer">
    <div class="offer-line">UP TO</div>
    <div class="offer-line">$2,000</div>
    <div class="offer-line">OFF</div>
    <div class="offer-date">till july 31st,2020</div>
  </div>

  <svg class="abs section-tab" viewBox="0 0 212 29" aria-hidden="true"><polygon points="0,0 195,0 212,29 0,29" fill="#6a4399"/></svg>
  <h2 class="abs section-title">Ortho Special</h2>

  <section class="abs service" style="left:32px;top:450px">
    <span class="service-icon is-olive"><svg width="20" height="20" viewBox="0 0 20 20"><path d="M3 8c2-3 12-3 14 0M3 12c2 3 12 3 14 0" fill="none" stroke="#fff" stroke-width="1.6"/><rect x="5" y="9" width="3" height="2" fill="#fff"/><rect x="12" y="9" width="3" height="2" fill="#fff"/><path d="M3 10h14" stroke="#fff" stroke-width="1"/></svg></span>
    <div class="service-text">
      <h3 class="service-title">Braces</h3>
      <p class="service-body">Straighter teeth for kids,<br>teens and adults...</p>
    </div>
  </section>
  <section class="abs service" style="left:270px;top:450px">
    <span class="service-icon is-purple"><svg width="20" height="20" viewBox="0 0 20 20"><circle cx="10" cy="6" r="3" fill="none" stroke="#fff" stroke-width="1.6"/><path d="M4 17c0-4 3-6 6-6s6 2 6 6" fill="none" stroke="#fff" stroke-width="1.6"/></svg></span>
    <div class="service-text">
      <h3 class="service-title">Free Consultation</h3>
      <p class="service-body">Meet our team and plan<br>your new smile...</p>
    </div>
  </section>
  <section class="abs service" style="left:32px;top:508px">
    <span class="service-icon is-purple"><svg width="20" height="20" viewBox="0 0 20 20"><path d="M3 8c1 6 13 6 14 0" fill="none" stroke="#fff" stroke-width="1.6"/><path d="M3 8h14" stroke="#fff" stroke-width="1.6"/></svg></span>
    <div class="service-text">
      <h3 class="service-title">Clear Aligners</h3>
      <p class="service-body">Quorventa aligners, almost<br>invisible treatment...</p>
    </div>
  </section>
  <section class="abs service" style="left:270px;top:508px">
    <span class="service-icon is-olive"><svg width="20" height="20" viewBox="0 0 20 20"><rect x="3" y="4" width="14" height="12" rx="1.5" fill="none" stroke="#fff" stroke-width="1.6"/><path d="M7 8c0 4 6 4 6 0" fill="none" stroke="#fff" stroke-width="1.4"/></svg></span>
    <div class="service-text">
      <h3 class="service-title">Free X-rays</h3>
      <p class="service-body">Included with every new<br>ortho consultation...</p>
    </div>
  </section>

  <p class="abs round-clock">Post Lockdown Ortho Special<br>Book Your Visit Today...</p>
  <span class="abs round-clock-rule"></span>
  <p class="abs about">Under a mask, no one sees your braces. Save up to $2,000 on braces or clear aligners, with a free consultation and X-rays, until July 31st 2020.</p>

  <span class="abs site-rule"></span>
  <div class="abs site-pill">www.yoursitename.com</div>

  <span class="abs consult-icon"></span>
  <p class="abs consult-label">Free Consultation &amp; X-rays</p>
  <p class="abs consult-phone">0123-456-789</p>

  <ul class="abs contact-list">
    <li><span class="contact-icon"><svg width="7" height="7" viewBox="0 0 10 10"><path d="M2 1l2 2-1 1.5c1 1.5 1.5 2 3 3L7.5 6l2 2-1.5 1.5C4 9 1 6 .5 2z" fill="#a4a152"/></svg></span><span>123 456 789<br>245 456 789</span></li>
    <li><span class="contact-icon"><svg width="7" height="7" viewBox="0 0 10 10"><rect x="1" y="2" width="8" height="6" fill="none" stroke="#a4a152" stroke-width="1.2"/><path d="M1 2l4 3 4-3" fill="none" stroke="#a4a152" stroke-width="1.2"/></svg></span><span>yourmail@mailbox.com</span></li>
    <li><span class="contact-icon"><svg width="7" height="7" viewBox="0 0 10 10"><path d="M1 5l4-4 4 4v4H1z" fill="none" stroke="#a4a152" stroke-width="1.3"/></svg></span><span>yourlocation like 65 street Road like Australia</span></li>
  </ul>
</main>
</body>
</html>
```